MOLVT Study flyer

I need help designing a flyer for a research study that will include brain imaging in adolescents. The info is in the attached document. The study is called the Marrowby Orchard Lantern Vesper Trail (MOLVT) study. Ideally this would be returned as a document that I can edit in the future as we will have several new recruitment phases (different age groups, etc. I also would love to have a logo designed as part of this project, but I recognize that might be a separate design request.

```html
<!DOCTYPE html>
<html lang="en">
<head>
<meta charset="utf-8">
<title>MOLVT Study Flyer</title>
<link href="https://fonts.googleapis.com/css2?family=Bebas+Neue&family=Poppins:wght@500;600;700;800&family=Lato:wght@400;700&display=swap" rel="stylesheet">
<style>
  :root{
    --navy:#0c1733;
    --teal:#17a39a;
    --purple:#5b3a9b;
    --orange:#f58220;
    --yellow:#fcc414;
    --sky:#1aa7e8;
    --mint:#e5f3f2;
    --ink:#1d1d1f;
    --white:#ffffff;
    --paper:#f4f4f2;
    --rule:#8a93a8;
  }
  *{box-sizing:border-box;margin:0;padding:0}
  html,body{width:950px;height:1200px;overflow:hidden;background:var(--white)}
  .flyer{position:relative;width:950px;height:1200px;overflow:hidden;background:var(--white);font-family:'Lato',sans-serif;color:var(--ink)}

  .hero-bg{position:absolute;left:0;top:0;width:950px;height:511px;background:linear-gradient(90deg,#fbfbfa 0%,var(--paper) 45%,#ececea 100%)}
  .hero-photo{position:absolute;left:520px;top:0;width:430px;height:511px;
    background:
      radial-gradient(ellipse 32% 48% at 45% 75%, #d9b59c 0%, rgba(217,181,156,0) 100%),
      radial-gradient(ellipse 42% 50% at 75% 38%, rgba(232,90,180,.5) 0%, rgba(252,196,20,.35) 45%, rgba(240,240,238,0) 100%),
      linear-gradient(90deg,#efefed 0%,#e6e4e1 40%,#e8d7c6 70%,#f1e2a8 100%)}

  .brand{position:absolute;left:91px;top:59px;display:flex;align-items:center;gap:10px}
  .brand-mark{width:34px;height:34px;background:var(--navy);border-radius:4px}
  .brand-name{font-family:'Poppins',sans-serif;font-weight:600;font-size:15px;line-height:1.15;color:var(--navy);width:130px}

  .headline{position:absolute;left:86px;top:137px;width:440px;height:270px;font-family:'Bebas Neue',sans-serif;font-weight:400;color:var(--white)}
  .headline .line{position:absolute;left:0;display:block;width:max-content;white-space:nowrap;font-size:84px;line-height:1;padding:12px 16px 4px 16px;transform:rotate(-3deg);transform-origin:left bottom}
  .line-1{top:0;background:var(--navy)}
  .line-2{top:86px;left:3px !important;background:var(--teal)}
  .line-3{top:170px;left:10px !important;background:var(--purple)}

  .subhead{position:absolute;left:116px;top:410px;font-family:'Bebas Neue',sans-serif;font-size:34px;line-height:1.2;color:var(--ink);transform:rotate(-3deg);transform-origin:left top}
  .subhead .accent{color:var(--orange)}

  .intro{position:absolute;left:65px;top:512px;width:818px;height:166px;background:var(--navy);border-radius:14px;display:flex;align-items:center}
  .intro-icon{width:247px;display:flex;justify-content:center}
  .intro-text{font-family:'Poppins',sans-serif;font-weight:500;font-size:15.5px;line-height:1.55;color:var(--white);width:520px}

  .section-title{font-family:'Poppins',sans-serif;font-weight:800;font-size:22px;line-height:1.2}
  .involves{position:absolute;left:95px;top:691px;width:420px}
  .involves .section-title{color:var(--purple)}
  .steps{list-style:none;margin-top:14px}
  .step{display:flex;align-items:center;gap:25px;margin-bottom:10px}
  .step-icon{flex:0 0 50px;width:50px;height:50px;border-radius:50%;display:flex;align-items:center;justify-content:center;margin-left:8px}
  .step-icon.teal{background:var(--teal)}
  .step-icon.purple{background:var(--purple)}
  .step-icon.sky{background:var(--sky)}
  .step-text{font-size:16px;line-height:1.3;width:305px}
  .step-text b{font-weight:700}

  .eligibility{position:absolute;left:520px;top:682px;width:356px;height:327px;background:var(--mint);border-radius:10px;padding:12px 15px 0 23px}
  .eligibility .section-title{font-size:22px}
  .eligibility .lead{color:var(--teal)}
  .eligibility .rest{color:var(--navy)}
  .criteria{list-style:none;margin-top:12px}
  .criterion{display:flex;gap:18px;align-items:flex-start;padding:11px 0;font-size:18px;line-height:1.25;font-weight:400;color:var(--ink)}
  .criterion + .criterion{border-top:1px solid var(--teal);margin-left:40px;margin-right:20px}
  .criterion + .criterion .tick{margin-left:-40px}
  .tick{flex:0 0 22px;margin-top:0}

  .footer{position:absolute;left:0;top:1027px;width:950px;height:173px;background:var(--navy);color:var(--white)}
  .contact-badge{position:absolute;left:61px;top:33px;width:107px;height:107px;border-radius:50%;background:var(--teal);display:flex;align-items:center;justify-content:center}
  .contact{position:absolute;left:196px;top:26px}
  .contact-title{font-family:'Poppins',sans-serif;font-weight:700;font-size:19px;line-height:1.2}
  .contact-note{font-family:'Poppins',sans-serif;font-size:12px;line-height:1.4;margin-top:2px}
  .contact-email{font-family:'Poppins',sans-serif;font-weight:500;font-size:17px;margin-top:6px}
  .divider{position:absolute;left:479px;top:25px;width:1px;height:126px;background:var(--rule)}
  .gift-badge{position:absolute;left:513px;top:40px;width:107px;height:107px;border-radius:50%;background:var(--yellow);display:flex;align-items:center;justify-content:center}
  .compensation{position:absolute;left:638px;top:44px;font-family:'Poppins',sans-serif;font-weight:700}
  .comp-title{font-size:23px;line-height:1}
  .comp-amount{display:flex;align-items:center;gap:10px;margin-top:2px}
  .comp-upto{font-size:19px;line-height:1.1}
  .comp-value{font-size:66px;font-weight:800;color:var(--yellow);line-height:1;letter-spacing:-2px}
</style>
</head>
<body>
<div class="flyer">
  <div class="hero-bg"></div>
  <div class="hero-photo" role="img" aria-label="Photo of a thoughtful teenage girl in front of a line-drawn brain bursting into colourful paint splashes and handwritten maths formulas"></div>

  <div class="brand">
    <div class="brand-mark"></div>
    <div class="brand-name">Halvern State University</div>
  </div>

  <h1 class="headline">
    <span class="line line-1">ARE YOU THE</span>
    <span class="line line-2">PARENT OF A</span>
    <span class="line line-3">CHILD AGE 10-17?</span>
  </h1>

  <p class="subhead">DO THEY <span class="accent">WORRY OR OVERTHINK</span><br>NEGATIVE EMOTIONS?</p>

  <section class="intro">
    <div class="intro-icon">
      <svg width="120" height="120" viewBox="0 0 120 120" fill="none" stroke-linecap="round">
        <g stroke="#fcc414" stroke-width="3">
          <line x1="60" y1="4" x2="60" y2="17"/><line x1="60" y1="103" x2="60" y2="116"/>
          <line x1="4" y1="60" x2="17" y2="60"/><line x1="103" y1="60" x2="116" y2="60"/>
          <line x1="31" y1="11" x2="37" y2="22"/><line x1="89" y1="11" x2="83" y2="22"/>
          <line x1="31" y1="109" x2="37" y2="98"/><line x1="89" y1="109" x2="83" y2="98"/>
          <line x1="11" y1="31" x2="22" y2="37"/><line x1="109" y1="31" x2="98" y2="37"/>
          <line x1="11" y1="89" x2="22" y2="83"/><line x1="109" y1="89" x2="98" y2="83"/>
        </g>
        <g stroke="#ffffff" stroke-width="3" stroke-linejoin="round">
          <path d="M58 30c-6-5-16-4-19 3-7 0-11 7-8 13-6 4-6 13 0 17-3 7 2 14 9 14 3 7 12 9 18 4z"/>
          <path d="M62 30c6-5 16-4 19 3 7 0 11 7 8 13 6 4 6 13 0 17 3 7-2 14-9 14-3 7-12 9-18 4z"/>
          <line x1="60" y1="30" x2="60" y2="81"/>
          <path d="M44 44c4 0 7 3 7 7M40 62c5-2 10 0 11 5M76 44c-4 0-7 3-7 7M80 62c-5-2-10 0-11 5"/>
        </g>
      </svg>
    </div>
    <p class="intro-text">Halvern State University researchers are seeking girls age 10-17 for a study about brain activity in emotions and decision-making and how they relate to puberty, anxiety and depression.</p>
  </section>

  <section class="involves">
    <h2 class="section-title">STUDY PARTICIPATION<br>INVOLVES:</h2>
    <ul class="steps">
      <li class="step">
        <span class="step-icon teal">
          <svg width="24" height="24" viewBox="0 0 24 24" fill="none" stroke="#fff" stroke-width="1.4"><rect x="4" y="7" width="16" height="12" rx="1"/><circle cx="12" cy="12" r="2.2"/><path d="M8.5 18c.5-2.5 6.5-2.5 7 0M2 20h20M9 4c2-1.5 4-1.5 6 0"/></svg>
        </span>
        <p class="step-text"><b>One one-hour interview</b><br>(online or in-person) where your child will discuss their thoughts</p>
      </li>
      <li class="step">
        <span class="step-icon purple">
          <svg width="22" height="24" viewBox="0 0 22 24" fill="none" stroke="#fff" stroke-width="1.4"><rect x="4" y="3" width="14" height="18" rx="1"/><path d="M7 7h2M11 7h5M7 11h2M11 11h5M7 15h2M11 15h5"/></svg>
        </span>
        <p class="step-text"><b>Online questionnaires</b><br>(parent and child)</p>
      </li>
      <li class="step">
        <span class="step-icon sky">
          <svg width="26" height="26" viewBox="0 0 26 26" fill="none" stroke="#fff" stroke-width="1.5"><circle cx="13" cy="13" r="10"/><path d="M13 7v6l4 3"/></svg>
        </span>
        <p class="step-text"><b>One two-hour visit</b> where your child will complete an MRI scan, answer questions about their puberty stage, and have a small hair sample taken to study puberty hormones</p>
      </li>
    </ul>
  </section>

  <section class="eligibility">
    <h2 class="section-title"><span class="lead">YOUR CHILD MAY</span><br><span class="rest">BE ELIGIBLE IF THEY:</span></h2>
    <ul class="criteria">
      <li class="criterion"><svg class="tick" width="22" height="22" viewBox="0 0 22 22"><circle cx="11" cy="11" r="11" fill="#17a39a"/><path d="M6.5 11.5l3 3 6-6.5" fill="none" stroke="#fff" stroke-width="1.8"/></svg><span>Are age 10-17</span></li>
      <li class="criterion"><svg class="tick" width="22" height="22" viewBox="0 0 22 22"><circle cx="11" cy="11" r="11" fill="#17a39a"/><path d="M6.5 11.5l3 3 6-6.5" fill="none" stroke="#fff" stroke-width="1.8"/></svg><span>Tend to worry or overthink negative thoughts</span></li>
      <li class="criterion"><svg class="tick" width="22" height="22" viewBox="0 0 22 22"><circle cx="11" cy="11" r="11" fill="#17a39a"/><path d="M6.5 11.5l3 3 6-6.5" fill="none" stroke="#fff" stroke-width="1.8"/></svg><span>Have not been diagnosed with psychosis, learning problems, or autism</span></li>
    </ul>
  </section>

  <footer class="footer">
    <div class="contact-badge">
      <svg width="50" height="38" viewBox="0 0 50 38" fill="none" stroke="#0c1733" stroke-width="3.5" stroke-linejoin="round"><rect x="2" y="2" width="46" height="34" rx="3"/><path d="M3 4l22 18L47 4M3 34l16-15M47 34L31 19"/></svg>
    </div>
    <div class="contact">
      <p class="contact-title">INTERESTED IN<br>PARTICIPATING?</p>
      <p class="contact-note">Want more information?<br>Please contact us!</p>
      <p class="contact-email">molvtstudy@halvern.edu</p>
    </div>
    <div class="divider"></div>
    <div class="gift-badge">
      <svg width="48" height="52" viewBox="0 0 48 52" fill="none" stroke="#0c1733" stroke-width="3" stroke-linejoin="round"><rect x="3" y="15" width="42" height="10"/><rect x="6" y="25" width="36" height="25"/><path d="M24 15v35M24 15c-4-10-14-12-14-5 0 4 8 5 14 5zM24 15c4-10 14-12 14-5 0 4-8 5-14 5z"/></svg>
    </div>
    <div class="compensation">
      <p class="comp-title">COMPENSATION</p>
      <div class="comp-amount">
        <span class="comp-upto">UP<br>TO</span>
        <span class="comp-value">$140</span>
      </div>
    </div>
  </footer>
</div>
</body>
</html>
```